Fable and Oat Mobile Bartending Website

Looking for an informational website for our mobile bartending business. We want to include features we like from another website that will help support our business.

Something with a similar set-up to https://wanderingtonicvan.example/

Coding

Coded - Design and coding required

```html
<!DOCTYPE html>
<html lang="en">
<head>
<meta charset="utf-8">
<title>Fable and Oat Mobile Bartending</title>
<link href="https://fonts.googleapis.com/css2?family=Montserrat:ital,wght@0,300;0,400;0,500;0,600;1,300&family=Josefin+Sans:wght@300;400&display=swap" rel="stylesheet">
<style>
:root{
  --ink:#1d1d1d;
  --muted:#555;
  --cream:#ece6d6;
  --cream-line:#3a3a3a;
  --grey-btn:#a9a9a9;
  --footer:#0b0b0b;
  --white:#fff;
  --star:#f3d37a;
}
*{box-sizing:border-box;margin:0;padding:0}
html,body{width:1200px;height:4996px;overflow:hidden;background:var(--white)}
body{position:relative;font-family:'Montserrat',sans-serif;color:var(--ink)}
.abs{position:absolute}
.btn{position:absolute;display:flex;align-items:center;justify-content:center;background:var(--cream);color:var(--ink);font-size:14px;letter-spacing:.3px;text-transform:uppercase}
.btn--grey{background:var(--grey-btn);color:var(--white)}
.photo{position:absolute}

/* header */
.topnav{top:28px;left:128px;display:flex;gap:34px;font-size:13px;text-transform:uppercase}
.mainnav{top:98px;font-size:15px;text-transform:uppercase}
.header-rule{top:71px;left:0;width:1200px;height:1px;background:#bbb}
.brand-mark{left:578px;top:18px;width:44px;height:44px;border-radius:50%;background:var(--ink)}
.brand{left:470px;top:86px;width:260px;text-align:center;background:var(--white)}
.brand__name{font-size:34px;font-weight:500;letter-spacing:1px;line-height:1}
.brand__sub{font-size:8px;letter-spacing:3px;margin-top:3px;font-weight:600}

/* hero */
.hero{top:147px;left:0;width:1200px;height:611px;background:linear-gradient(120deg,#2c2a26,#5a4736 45%,#3a3329 70%,#1f1d1b)}
.hero__title{left:127px;top:515px;color:var(--white);font-size:33px;font-weight:500;line-height:41px;letter-spacing:.5px}

/* tiles */
.tile-label{position:absolute;left:50%;top:50%;transform:translate(-50%,-50%);background:var(--cream);outline:1px solid var(--cream-line);outline-offset:-5px;padding:12px 28px;font-size:17px;white-space:nowrap;text-transform:uppercase}

.section-title{position:absolute;left:0;width:1200px;text-align:center;font-size:31px;font-weight:500;letter-spacing:.5px;line-height:37px;text-transform:uppercase}
.para{position:absolute;text-align:center;font-size:15px;line-height:20px;color:var(--muted);font-weight:300;font-family:'Josefin Sans',sans-serif}

/* testimonial */
.card{left:204px;top:2355px;width:793px;height:303px;background:var(--white);box-shadow:0 0 22px rgba(0,0,0,.08)}
.avatar{left:540px;top:2326px;width:120px;height:120px;border-radius:50%;background:linear-gradient(#3a5a6a,#8a6a50)}
.quote{left:260px;top:2495px;width:680px;text-align:center;font-style:italic;font-weight:300;font-size:15px;line-height:22px;color:var(--muted)}

/* companies */
.company{position:absolute;top:3528px;width:170px;font-size:20px;line-height:24px;font-weight:500;text-align:center;color:var(--ink)}

/* footer */
.footer{top:4617px;left:0;width:1200px;height:379px;background:var(--footer)}
.footer-heading{position:absolute;top:4682px;color:var(--white);font-size:20px;font-weight:500;text-transform:uppercase}
.contact-row{position:absolute;left:126px;display:flex;gap:18px;font-family:'Josefin Sans',sans-serif;font-size:15px;line-height:19px;color:var(--white)}
.contact-row svg{flex:none;margin-top:4px}
.quick{position:absolute;left:863px;top:4722px;font-family:'Josefin Sans',sans-serif;font-size:16px;line-height:31px;color:var(--white)}
.social{position:absolute;top:4868px;left:548px;display:flex;gap:18px}
.social span{width:20px;height:20px;border-radius:50%;background:var(--white);display:block}
</style>
</head>
<body>

<!-- header -->
<nav class="abs topnav"><span>About</span><span>FAQ</span><span>Cart Co.</span><span>Account</span></nav>
<div class="btn" style="left:870px;top:20px;width:203px;height:38px;font-size:13px">Request Our Services</div>
<div class="abs header-rule"></div>
<div class="abs brand-mark"></div>
<div class="abs brand">
  <div class="brand__name">FABLE &amp; OAT</div>
  <div class="brand__sub">MOBILE BARTENDING</div>
</div>
<nav class="abs mainnav" style="left:125px">Packages + Bars</nav>
<nav class="abs mainnav" style="left:325px">Cocktail Menu</nav>
<nav class="abs mainnav" style="left:743px">Alcohol Calculator</nav>
<nav class="abs mainnav" style="left:988px;display:flex;align-items:center;gap:5px">
  <svg width="12" height="13" viewBox="0 0 12 13"><rect x="1" y="4" width="10" height="9" fill="#1d1d1d"/><path d="M3.5 4V3a2.5 2.5 0 0 1 5 0v1" stroke="#1d1d1d" fill="none" stroke-width="1.4"/></svg>CART(0)
</nav>

<!-- hero -->
<div class="photo hero" role="img" aria-label="Friends ordering drinks at a mobile bar truck under string lights at dusk"></div>
<h1 class="abs hero__title">MOBILE BARTENDING<br>WHEREVER. YOU. WANT.</h1>
<div class="btn" style="left:127px;top:610px;width:278px;height:52px;font-size:16px">Book Your Event Today</div>

<!-- feature tiles -->
<div class="photo" style="left:0;top:776px;width:388px;height:328px;background:linear-gradient(135deg,#f6c6cc,#f08a6c 60%,#e9b9b4)" role="img" aria-label="Grapefruit cocktails with pink straws"><div class="tile-label">Packages + Bars</div></div>
<div class="photo" style="left:406px;top:776px;width:388px;height:328px;background:linear-gradient(135deg,#e8d7bf,#f2b44a 55%,#d99a55)" role="img" aria-label="Golden cocktails garnished with rosemary"><div class="tile-label">Cocktail Menu</div></div>
<div class="photo" style="left:812px;top:776px;width:388px;height:328px;background:linear-gradient(135deg,#c9b79a,#e07a3a 55%,#a35a3a)" role="img" aria-label="Hands toasting with citrus cocktails"><div class="tile-label">Alcohol Calculator</div></div>

<!-- about -->
<div class="abs" style="left:565px;top:1210px;width:70px;height:70px;border-radius:50%;background:var(--ink)"></div>
<h2 class="section-title" style="top:1338px">About Fable and Oat Mobile Bartending</h2>
<p class="para" style="left:180px;top:1409px;width:840px">Lorem ipsum dolor sit amet, consectetur adipiscing elit, sed do eiusmod tempor incididunt ut labore et do lore magna aliquaiuis ipsum suspendisse ultrices gravida. Risus commodo viverra maecenas accumsan lacus vencididunt ut labore et dolore magna aliqua. Quis ipsum suspendisse ultrices gra ida. Risus commodo viverra maecenas accumsan lacus vel facilis commodo v commodo viverra maecenas accumsan lacus vencididunt ut labore et dolore magna aliqua. Quis ipsum suspendisse ultrices gra ida. Risus commodo viverra maecenas accumsan lacus vel facilis commodo viverra maecenas acis.</p>
<div class="btn" style="left:535px;top:1566px;width:130px;height:43px;font-size:14px">Read More</div>

<!-- photo strip -->
<div class="photo" style="left:0;top:1697px;width:326px;height:468px;background:linear-gradient(160deg,#d99a3a,#8a4a1a 60%,#5a3a22)" role="img" aria-label="Whiskey cocktail over ice with lime"></div>
<div class="photo" style="left:327px;top:1697px;width:325px;height:468px;background:linear-gradient(160deg,#6a6a6a,#3a3a3a 60%,#2a2a2a)" role="img" aria-label="Hand holding a smoking cocktail glass"></div>
<p class="abs" style="left:358px;top:2068px;color:#fff;font-size:25px;line-height:30px;font-weight:500">INTIMATE<br>COCKTAIL PARTY?</p>
<div class="photo" style="left:652px;top:1697px;width:326px;height:468px;background:linear-gradient(160deg,#c9ccd0,#e8e8ea 50%,#b8bcc0)" role="img" aria-label="Row of wine glasses with raspberries and mint"></div>
<div class="photo" style="left:978px;top:1697px;width:222px;height:468px;background:linear-gradient(160deg,#d8c8b8,#e8a46a 55%,#c48a5a)" role="img" aria-label="Citrus cocktail with mint garnish"></div>

<!-- testimonials -->
<h2 class="section-title" style="top:2245px">Client Testimonials</h2>
<div class="abs card"></div>
<div class="photo avatar" role="img" aria-label="Client portrait"></div>
<p class="abs" style="left:0;width:1200px;top:2464px;text-align:center;font-size:16px;font-weight:600">MARISOL T</p>
<p class="abs quote">Lorem ipsum dolor sit ameconsectetur adipiscing elitse do eiusmod tempor idnt ut labore et dolore mag na aliquaLorem ipsum dolor sit ameconsectetur adipiscing elitse do eiusmod tempor incid idnt ut labore et dolore mag na aliqua. Quis ipsum suspen disse ultrices gravida. is ipsum suspen ds gravida.</p>
<svg class="abs" style="left:533px;top:2600px" width="134" height="22" viewBox="0 0 134 22" fill="#f3d37a">
  <g id="star"><polygon points="11,1 14,8 21,8.5 15.5,13 17.5,20 11,16 4.5,20 6.5,13 1,8.5 8,8"/></g>
  <use href="#star" x="28"/><use href="#star" x="56"/><use href="#star" x="84"/><use href="#star" x="112"/>
</svg>
<svg class="abs" style="left:145px;top:2498px" width="12" height="20" viewBox="0 0 12 20"><path d="M10 2 2 10l8 8" stroke="#888" stroke-width="2" fill="none"/></svg>
<svg class="abs" style="left:1034px;top:2498px" width="12" height="20" viewBox="0 0 12 20"><path d="M2 2l8 8-8 8" stroke="#888" stroke-width="2" fill="none"/></svg>

<!-- request band -->
<div class="photo" style="left:0;top:2774px;width:1200px;height:501px;background:linear-gradient(90deg,#d9cfc4,#ede8e2 40%,#f1f1f1 65%,#f2f2f2)" role="img" aria-label="Elegant table setting with glasses, roses and fruit"></div>
<p class="abs" style="left:560px;top:2948px;width:508px;text-align:right;font-size:31px;line-height:38px;font-weight:500">REQUEST OUR SERVICES<br>FOR YOUR NEXT EVENT!</p>
<div class="btn btn--grey" style="left:828px;top:3041px;width:239px;height:48px;font-size:14px">Request Our Services</div>

<!-- companies -->
<h2 class="section-title" style="top:3373px">Companies Who<br>Have Booked Our Services</h2>
<div class="company" style="left:208px;top:3540px">Ridewell</div>
<div class="company" style="left:390px">Lena<br>Marlowe</div>
<div class="company" style="left:572px">Northgate<br>Pay</div>
<div class="company" style="left:776px">Coastline<br>Threads</div>

<!-- gallery -->
<h2 class="section-title" style="top:3742px">Our Gallery</h2>
<p class="para" style="left:190px;top:3796px;width:820px">Lorem ipsum dolor sit amet, consectetur adipiscing elit, sed do eiusmod tempor incididunt ut labore et dolore magna aliquaiuis ipsum suspendisse ultrices gravida. Risus commodo viverra maecenas.</p>
<div class="photo" style="left:108px;top:3880px;width:233px;height:306px;background:linear-gradient(170deg,#e8c4a0,#e0762a 55%,#8a5a3a)" role="img" aria-label="Orange cocktails at sunset"></div>
<div class="photo" style="left:359px;top:3880px;width:233px;height:306px;background:linear-gradient(170deg,#d8d4ce,#e8b8a8 50%,#c8c0b6)" role="img" aria-label="Overhead view of assorted cocktails"></div>
<div class="photo" style="left:611px;top:3880px;width:233px;height:306px;background:linear-gradient(170deg,#6a5a4a,#e89a86 50%,#5a4030)" role="img" aria-label="Pink gin cocktails with rosemary"></div>
<div class="photo" style="left:861px;top:3880px;width:233px;height:306px;background:linear-gradient(170deg,#cfc6b0,#ece2c4 50%,#b8a890)" role="img" aria-label="Couple toasting with creamy cocktails"></div>
<div class="btn" style="left:528px;top:4232px;width:144px;height:47px;font-size:14px">Follow Us</div>

<!-- newsletter -->
<div class="photo" style="left:0;top:4300px;width:1200px;height:317px;background:linear-gradient(180deg,#fff,#f7f3ea 50%,#f3eee2)" role="img" aria-label="Soft blurred citrus drinks backdrop"></div>
<h2 class="section-title" style="top:4360px">Let’s Stay Connected</h2>
<p class="para" style="left:190px;top:4410px;width:820px">Lorem ipsum dolor sit amet, consectetur adipiscing elit, sed do eiusmod tempor incididunt ut labore et dolore magna aliquaiuis ipsum suspendisse ultrices gravida. Risus commodo viverra maecenas.</p>
<div class="abs" style="left:283px;top:4483px;width:475px;height:51px;border:1px solid #8a8270;padding:17px 14px;font-size:13px;color:#bbb">EMAIL:</div>
<div class="btn btn--grey" style="left:774px;top:4483px;width:144px;height:51px;font-size:14px">Sign Up</div>

<!-- footer -->
<footer class="abs footer"></footer>
<h4 class="footer-heading" style="left:126px">Contact Us</h4>
<div class="contact-row" style="top:4728px">
  <svg width="18" height="18" viewBox="0 0 24 24" fill="#fff"><path d="M6.6 10.8a15 15 0 0 0 6.6 6.6l2.2-2.2a1 1 0 0 1 1-.25 11.4 11.4 0 0 0 3.6.57 1 1 0 0 1 1 1V20a1 1 0 0 1-1 1A17 17 0 0 1 3 4a1 1 0 0 1 1-1h3.5a1 1 0 0 1 1 1c0 1.25.2 2.45.57 3.57a1 1 0 0 1-.25 1z"/></svg>
  <div>Call Us:<br>000-555-0148</div>
</div>
<div class="contact-row" style="top:4800px">
  <svg width="20" height="16" viewBox="0 0 20 16"><rect width="20" height="16" rx="2" fill="#fff"/><path d="M1 2l9 7 9-7" stroke="#0b0b0b" stroke-width="2" fill="none"/></svg>
  <div>Email:<br>info@FableandOat.example</div>
</div>
<div class="contact-row" style="top:4862px">
  <svg width="18" height="24" viewBox="0 0 18 24"><path d="M9 0a9 9 0 0 1 9 9c0 6-9 15-9 15S0 15 0 9a9 9 0 0 1 9-9z" fill="#fff"/><circle cx="9" cy="9" r="3.5" fill="#0b0b0b"/></svg>
  <div>Address: Fable and Oat Lane<br>Willow Bend 10482</div>
</div>
<div class="abs" style="left:578px;top:4712px;width:48px;height:48px;border-radius:50%;background:#fff"></div>
<div class="abs" style="left:450px;top:4772px;width:300px;text-align:center;color:#fff">
  <div style="font-size:40px;font-weight:500;letter-spacing:1px;line-height:1">FABLE &amp; OAT</div>
  <div style="font-size:9px;letter-spacing:3px;margin-top:4px;font-weight:600">MOBILE BARTENDING</div>
</div>
<div class="social"><span></span><span></span><span></span></div>
<h4 class="footer-heading" style="left:863px">Quick Links</h4>
<div class="quick">
  About Fable and Oat<br>Our Fable and Oat Team<br>Packages &amp; Bar<br>Cocktail Menu<br>Alcohol Calculator<br>Request Our Services
</div>
<p class="abs" style="left:0;width:1200px;top:4943px;text-align:center;color:#fff;font-family:'Josefin Sans',sans-serif;font-size:15px">Copyright 2023 All rights are reserved.</p>

</body>
</html>
```